Corbrook Estates LLC stationary for a real estate property management company.

Create stationary (letterhead, envelopes, business cards) using Corbrook Estates LLC logo as primary creative element. Stationary design needs to be horizontal, leaving as much space as possible for correspondence copy. See attached Creative Brief and past stationary files for details.

Target Market(s)

Prospective apartment residents and current residents, vendors, and government agencies.

Industry/Entity Type

Property Management

Contact Information for Business Card

Business card employee title: Property Manager. Should include address, phone, fax, email, website, slogan, and Corbrook Estates logo.

Font styles to use
Sans Serif

Colors
0592cd
000000

Requirements
Must have
• Tone should be conservative, institutional, business (i.e. banking, finance, real estate). Must include: address, phone, fax, website, and slogan (see attached Creative Brief). Should be a horizontal design, leaving as much room as possible for letter correspondence copy.
Nice to have
• Please use an Arial or Helvetica style font.
Should not have
• Letterhead layout should leave as much room as possible for copy.

```html
<!DOCTYPE html>
<html lang="en">
<head>
<meta charset="utf-8">
<title>Corbrook Estates LLC – Stationery</title>
<link href="https://fonts.googleapis.com/css2?family=Roboto+Condensed:wght@400;700&display=swap" rel="stylesheet">
<style>
  :root {
    --brand-blue: #0592cd;
    --brand-black: #000000;
    --brand-navy: #1d3b9a;
    --paper: #f3f4f2;
    --backdrop: #e4e5e7;
    --ink: #1c1c1c;
  }
  * { box-sizing: border-box; margin: 0; padding: 0; }
  html, body { width: 1200px; height: 1200px; overflow: hidden; }
  body {
    background: var(--backdrop);
    font-family: "Roboto Condensed", Arial, sans-serif;
    color: var(--ink);
    position: relative;
  }
  .piece { position: absolute; background: var(--paper); overflow: hidden; box-shadow: 0 2px 6px rgba(0,0,0,.12); }
  .band { position: absolute; left: 0; top: 0; width: 100%; display: block; }
  .band .blue { fill: var(--brand-blue); }
  .band .black { fill: var(--brand-black); }

  .wordmark { position: absolute; display: flex; align-items: center; white-space: nowrap; font-weight: 700; letter-spacing: .01em; }
  .wordmark .mark-square { flex: none; background: currentColor; }
  .wordmark--navy { color: var(--brand-navy); }
  .wordmark--white { color: #fff; }

  .contact { position: absolute; font-size: 8px; line-height: 1.45; }
  .contact .address { margin-bottom: 6px; }
  .contact .row { display: flex; align-items: center; gap: 5px; }
  .contact .icon { width: 6px; height: 6px; flex: none; fill: var(--brand-blue); }
  .contact .small { font-size: .82em; }

  /* business card front */
  .card-front { left: 51px; top: 109px; width: 196px; height: 137px; background: var(--brand-blue); }
  .card-front .url { position: absolute; bottom: 10px; width: 100%; text-align: center; color: #dbeefa; font-size: 5px; }

  /* business card back */
  .card-back { left: 51px; top: 276px; width: 196px; height: 136px; }
  .card-back .person { position: absolute; right: 8px; top: 54px; text-align: right; }
  .card-back .person .name { color: var(--brand-blue); font-weight: 700; font-size: 9px; }
  .card-back .person .title { font-size: 5px; }
  .card-back .contact { font-size: 6px; }

  /* letterhead */
  .letterhead { left: 307px; top: 158px; width: 367px; height: 630px; }

  /* envelope with address block */
  .envelope-address { left: 742px; top: 109px; width: 410px; height: 249px; }

  /* presentation folder */
  .folder { left: 742px; top: 384px; width: 412px; height: 664px; background: var(--brand-blue); border-radius: 0 6px 6px 0; }
  .folder .url { position: absolute; left: 0; right: 0; top: 598px; text-align: center; color: #fff; font-size: 19px; }

  /* envelope with flap */
  .envelope-flap { left: 265px; top: 833px; width: 410px; height: 249px; }
  .envelope-flap .flap { position: absolute; left: 0; top: 0; width: 100%; height: 63px; background: var(--brand-blue); border-radius: 0 0 10px 10px; }
</style>
</head>
<body>

<!-- Business card, front -->
<section class="piece card-front">
  <div class="wordmark wordmark--white" style="left:30px;top:58px;font-size:13px;gap:5px;">
    <span class="mark-square" style="width:12px;height:12px;"></span>CORBROOK ESTATES LLC
  </div>
  <p class="url">www.corbrookestates.us</p>
</section>

<!-- Business card, back -->
<section class="piece card-back">
  <svg class="band" viewBox="0 0 196 34" height="34" preserveAspectRatio="none">
    <path class="black" d="M105 28 C122 28 124 15 140 15 H196 V28 Z"/>
    <path class="blue" d="M0 0 H196 V15 H142 C126 15 126 34 108 34 H0 Z"/>
  </svg>
  <div class="wordmark wordmark--navy" style="left:8px;top:56px;font-size:8.5px;gap:3px;">
    <span class="mark-square" style="width:8px;height:8px;"></span>CORBROOK ESTATES LLC
  </div>
  <div class="person">
    <p class="name">ELLEN WHITCOMBE</p>
    <p class="title">PROPERTY MANAGER</p>
  </div>
  <div class="contact" style="left:8px;top:86px;">
    <p class="row"><svg class="icon" viewBox="0 0 6 6"><rect x="1.5" y="0" width="3" height="6" rx=".6"/></svg>555-014-2271</p>
    <p class="row"><svg class="icon" viewBox="0 0 6 6"><rect x="0" y="2" width="6" height="4"/><rect x="1.5" y="0" width="3" height="2"/></svg>555-014-2289</p>
    <p class="row small"><svg class="icon" viewBox="0 0 6 6"><rect x="0" y="1" width="6" height="4"/></svg>ellen@corbrookestates.us</p>
    <p class="row small"><svg class="icon" viewBox="0 0 6 6"><circle cx="3" cy="3" r="3"/></svg>www.corbrookestates.us</p>
  </div>
  <div class="contact" style="right:8px;top:104px;font-size:5.5px;text-align:left;">
    <p>2218 Alder Avenue # 204</p>
    <p>Fairview, CA 90417</p>
  </div>
</section>

<!-- Letterhead -->
<section class="piece letterhead">
  <svg class="band" viewBox="0 0 367 65" height="65" preserveAspectRatio="none">
    <path class="black" d="M180 54 C200 54 200 30 222 30 H367 V54 Z"/>
    <path class="blue" d="M0 0 H367 V30 H224 C202 30 204 65 180 65 H0 Z"/>
  </svg>
  <div class="wordmark wordmark--navy" style="left:30px;top:112px;font-size:17px;gap:6px;">
    <span class="mark-square" style="width:15px;height:15px;"></span>CORBROOK ESTATES LLC
  </div>
  <div class="contact" style="left:247px;top:76px;">
    <p class="address">2218 Alder Avenue # 204<br>Fairview, CA 90417</p>
    <p class="row"><svg class="icon" viewBox="0 0 6 6"><rect x="1.5" y="0" width="3" height="6" rx=".6"/></svg>555-014-2271</p>
    <p class="row"><svg class="icon" viewBox="0 0 6 6"><rect x="0" y="2" width="6" height="4"/><rect x="1.5" y="0" width="3" height="2"/></svg>555-014-2289</p>
    <p class="row small"><svg class="icon" viewBox="0 0 6 6"><rect x="0" y="1" width="6" height="4"/></svg>ellen@corbrookestates.us</p>
    <p class="row small"><svg class="icon" viewBox="0 0 6 6"><circle cx="3" cy="3" r="3"/></svg>www.corbrookestates.us</p>
  </div>
</section>

<!-- Envelope, address side -->
<section class="piece envelope-address">
  <svg class="band" viewBox="0 0 410 74" height="74" preserveAspectRatio="none">
    <path class="black" d="M215 62 C235 62 238 35 262 35 H410 V62 Z"/>
    <path class="blue" d="M0 0 H410 V35 H264 C240 35 240 74 216 74 H0 Z"/>
  </svg>
  <div class="wordmark wordmark--navy" style="left:15px;top:108px;font-size:15px;gap:5px;">
    <span class="mark-square" style="width:13px;height:13px;"></span>CORBROOK ESTATES LLC
  </div>
  <div class="contact" style="left:318px;top:72px;font-size:7px;">
    <p class="address">2218 Alder Avenue # 204<br>Fairview, CA 90417</p>
    <p class="row"><svg class="icon" viewBox="0 0 6 6"><rect x="1.5" y="0" width="3" height="6" rx=".6"/></svg>555-014-2271</p>
    <p class="row"><svg class="icon" viewBox="0 0 6 6"><rect x="0" y="2" width="6" height="4"/><rect x="1.5" y="0" width="3" height="2"/></svg>555-014-2289</p>
    <p class="row small"><svg class="icon" viewBox="0 0 6 6"><rect x="0" y="1" width="6" height="4"/></svg>ellen@corbrookestates.us</p>
    <p class="row small"><svg class="icon" viewBox="0 0 6 6"><circle cx="3" cy="3" r="3"/></svg>www.corbrookestates.us</p>
  </div>
</section>

<!-- Presentation folder -->
<section class="piece folder">
  <div class="wordmark wordmark--white" style="left:34px;top:122px;font-size:29px;gap:9px;">
    <span class="mark-square" style="width:24px;height:24px;"></span>CORBROOK ESTATES LLC
  </div>
  <p class="url">www.corbrookestates.us</p>
</section>

<!-- Envelope, flap side -->
<section class="piece envelope-flap">
  <div class="flap">
    <div class="wordmark wordmark--white" style="left:0;right:0;justify-content:center;top:22px;font-size:16px;gap:6px;">
      <span class="mark-square" style="width:14px;height:14px;"></span>CORBROOK ESTATES LLC
    </div>
  </div>
</section>

</body>
</html>
```